Bus backs advertising

We need a strong design that can work over a number of messages on the backs of buses.
We are a property investment company.
We need strong, corporate branding. Plus designs that could be translated through to the various bus back specs
Plus could also work on the side of the bus.
Our corporate colours are Black, silver and dark orange.
there are 4 change outs of headlines but All I need is on e strong graphic design at this point
I will attach what I received - which I dont like and I will attach a logo
here is the copy for each variation....
1. Fact #29
You can have
a passive income long before
you retire…..

Find out how
Call 0800 GLIMMER
www.tarvenholdings.co.nz

Logo

2. Fact # 31
It is possible to buy
an investment property
without a cash deposit…

Find out how
Call 0800 GLIMMER

Logo

3. Fact #18
You can have a passive income
Long before
You retire….

Find out how
Call 0800 GLIMMER

Logo

4. Fact #10
Pay for your children’s
Future education without
Cash in the bank…

Find out how
Call 0800 GLIMMER
OR www.tarvenholdings.co.nz

Logo

```html
<!DOCTYPE html>
<html lang="en">
<head>
<meta charset="utf-8">
<title>Fact #31 – Bus Back</title>
<link rel="stylesheet" href="https://fonts.googleapis.com/css2?family=Arvo:wght@400;700&family=Roboto+Slab:wght@300;700&display=swap">
<style>
  :root {
    --orange: #ef4a23;
    --orange-deep: #d8361c;
    --ember: #7a1a0c;
    --black: #000000;
    --white: #ffffff;
    --silver-light: #eef0f3;
    --silver-dark: #9aa1aa;
    --page: #ffffff;
  }
  html, body { margin: 0; padding: 0; overflow: hidden; }
  body { background: var(--page); }
  .canvas {
    position: relative; width: 1200px; height: 1200px;
    overflow: hidden; background: var(--page);
  }
  .bus-back {
    position: absolute; left: 210px; top: 183px;
    width: 804px; height: 825px;
    border-radius: 34px 34px 0 0;
    overflow: hidden; background: var(--orange);
  }
  .sky-art {
    position: absolute; left: 0; top: 0; width: 804px; height: 552px;
    background: linear-gradient(180deg, var(--orange-deep) 0%, var(--orange) 30%, var(--orange) 56%, var(--ember) 80%, var(--black) 100%);
  }
  .base-band {
    position: absolute; left: 0; top: 552px; width: 804px; height: 273px;
    background: var(--black);
  }
  .side-trim { position: absolute; top: 520px; width: 150px; height: 305px; }
  .side-trim--left { left: 0; }
  .side-trim--right { right: 0; transform: scaleX(-1); }
  .fact-title {
    position: absolute; left: 86px; top: 32px; margin: 0;
    font-family: "Arvo", Georgia, serif; font-weight: 700;
    font-size: 80px; line-height: 1; color: var(--white);
    letter-spacing: -1px;
  }
  .headline {
    position: absolute; left: 88px; top: 138px; margin: 0;
    font-family: "Arvo", Georgia, serif; font-weight: 700;
    font-size: 51px; line-height: 64px; color: var(--black);
    letter-spacing: -0.5px;
  }
  .cta {
    position: absolute; left: 0; top: 556px; width: 804px;
    text-align: center; color: var(--white);
  }
  .cta__lead {
    margin: 0; font-family: "Roboto Slab", Georgia, serif;
    font-weight: 300; font-size: 28px; line-height: 40px;
  }
  .cta__call {
    margin: 6px 0 0; font-family: "Roboto Slab", Georgia, serif;
    font-weight: 300; font-size: 40px; line-height: 48px;
  }
  .cta__number { font-family: "Arvo", Georgia, serif; font-weight: 700; color: var(--orange); }
  .cta__web {
    margin: 2px 0 0; font-family: "Arvo", Georgia, serif;
    font-weight: 700; font-size: 26px; line-height: 34px;
  }
  .brand {
    position: absolute; left: 0; top: 728px; width: 804px;
    display: flex; justify-content: center; align-items: center; gap: 12px;
  }
  .brand__mark { width: 22px; height: 22px; border-radius: 50%; background: var(--silver-dark); }
  .brand__name {
    font-family: "Arvo", Georgia, serif; font-weight: 700;
    font-size: 28px; color: var(--silver-light); letter-spacing: 1px;
  }
</style>
</head>
<body>
<div class="canvas">
  <div class="bus-back">
    <div class="sky-art" role="img" aria-label="Orange sky with decorative circles above a black city skyline silhouette with towers, a bridge and a setting sun"></div>
    <div class="base-band"></div>

    <svg class="side-trim side-trim--left" viewBox="0 0 150 305" role="img" aria-label="Silver side trim with coloured indicator lights">
      <defs>
        <linearGradient id="trimLeft" x1="0" y1="0" x2="1" y2="1">
          <stop offset="0" stop-color="var(--silver-dark)"/>
          <stop offset="1" stop-color="var(--silver-light)"/>
        </linearGradient>
      </defs>
      <path d="M0 0 Q130 120 142 305 L0 305 Z" fill="url(#trimLeft)"/>
    </svg>
    <svg class="side-trim side-trim--right" viewBox="0 0 150 305" role="img" aria-label="Silver side trim with coloured indicator lights">
      <defs>
        <linearGradient id="trimRight" x1="0" y1="0" x2="1" y2="1">
          <stop offset="0" stop-color="var(--silver-dark)"/>
          <stop offset="1" stop-color="var(--silver-light)"/>
        </linearGradient>
      </defs>
      <path d="M0 0 Q130 120 142 305 L0 305 Z" fill="url(#trimRight)"/>
    </svg>

    <h1 class="fact-title">Fact #31</h1>
    <p class="headline">It is possible to buy<br>an investment property<br>without a cash deposit…</p>

    <div class="cta">
      <p class="cta__lead">Find out how</p>
      <p class="cta__call">Call <span class="cta__number">0800 GLIMMER</span></p>
      <p class="cta__web">www.tarvenholdings.co.nz</p>
    </div>

    <div class="brand">
      <span class="brand__mark"></span>
      <span class="brand__name">Tarven Holdings</span>
    </div>
  </div>
</div>
</body>
</html>
```